Online-Marketing Material für Recruiting-Plattform
Zielgruppe
Recruiting-Plattform für Physiotherapeuten. Wir sind Vermittler.
Aufgabenstellung
Ich benötige ein 2er Set aus Social-Media-Templates, das wir als Basis für Recruiting-Ads nutzen können.
Variante 1: (1080 x 1350) mit jeweils 285 Pixel Safe Space oben und unten (hier keine wichtigen Elemente).
Wichtig: Es handelt sich um ein Template. Daher muss es mit verschiedenen Elementen und Fotos funktionieren.
Die Elemente werden später durch variable Inhalte gesetzt. Ziel ist es, ein möglichst flexibles Format zu schaffen,
das mit unterschiedlichen Inhalten funktioniert.
Bitte orientiere dich am Grunddesign der Website kurapunkt.de
Elemente und zugehörige Beispiele sind
1. Foto in querformat | Beispiel als Download)
2. Jobtitel als Headline | (Physiotherapeut (m/w/d)
3. Subtitle | Werde Teil eines wachsenden Teams
4. Arbeitszeitmodell | Vollzeit, Teilzeit
3. Ort | Hannover
4. 3 x Highlights | 1. Betriebliche Krankenversicherung 2. Pedalo 3. Gehalt bis zu 4.500 EUR
(Die Highlight variieren thematisch, daher hier bitte nur mit thematisch-neutralen Icons arbeiten.
5. Logo des Arbeitgebers (velmo) auf weiß
Variante 2 mit Foto in hochformat

```html
<!DOCTYPE html>
<html lang="de">
<head>
<meta charset="utf-8">
<title>Stellenanzeige Physiotherapeut – velmo</title>
<link rel="stylesheet" href="https://fonts.googleapis.com/css2?family=Archivo+Black&family=Archivo:wght@500;700&family=Caveat:wght@700&display=swap">
<style>
  :root {
    --paper-light: #f1f1f0;
    --paper-mid: #dcdcda;
    --ink: #111111;
    --berry: #c04b76;
    --white: #ffffff;
    --photo-light: #e9ebec;
    --photo-mid: #b7bcc0;
  }
  * { box-sizing: border-box; margin: 0; padding: 0; }
  html, body { width: 960px; height: 1200px; overflow: hidden; }
  body { background: var(--paper-light); }

  .ad {
    position: relative;
    width: 960px;
    height: 1200px;
    overflow: hidden;
    background: radial-gradient(ellipse at 30% 20%, var(--paper-light) 0%, var(--paper-mid) 100%);
    font-family: "Archivo", Arial, sans-serif;
    color: var(--ink);
  }

  .gender-tag {
    position: absolute;
    left: 55px; top: 140px;
    font-family: "Archivo Black", Arial, sans-serif;
    font-size: 30px;
    letter-spacing: 0.5px;
  }

  .job-title {
    position: absolute;
    left: 52px; top: 192px;
    font-family: "Archivo Black", Arial, sans-serif;
    font-size: 94px;
    line-height: 90px;
    letter-spacing: 1px;
    text-transform: uppercase;
  }

  .work-model {
    position: absolute;
    left: 55px; top: 411px;
    width: 398px; height: 65px;
    border-radius: 22px;
    background: var(--berry);
    display: flex; align-items: center; justify-content: center;
    font-weight: 700;
    font-size: 30px;
  }

  .subtitle {
    position: absolute;
    left: 55px; top: 535px;
    font-family: "Caveat", cursive;
    font-weight: 700;
    font-size: 46px;
    line-height: 52px;
    transform: rotate(-2deg);
    transform-origin: left top;
  }

  .brand {
    position: absolute;
    left: 700px; top: 128px;
    display: flex; align-items: center; gap: 12px;
  }
  .brand-name {
    font-family: "Archivo", Arial, sans-serif;
    font-weight: 700;
    font-size: 44px;
    line-height: 1;
    color: var(--ink);
  }
  .brand-mark {
    width: 18px; height: 18px;
    background: var(--berry);
  }

  .berry-panel {
    position: absolute;
    left: 0; top: 692px;
    width: 960px; height: 508px;
    background: var(--berry);
    border-top-left-radius: 72px;
  }

  .highlights {
    position: absolute;
    left: 82px; top: 774px;
    list-style: none;
  }
  .highlights li {
    display: flex; align-items: center; gap: 18px;
    height: 43px;
    color: var(--white);
    font-weight: 700;
    font-size: 25px;
    text-transform: uppercase;
  }
  .highlights svg { width: 24px; height: 24px; flex: none; }

  .dot-grid {
    position: absolute;
    left: 76px; top: 1025px;
  }

  .photo {
    position: absolute;
    left: 500px; top: 505px;
    width: 460px; height: 562px;
    border-radius: 28px 0 0 28px;
    background: linear-gradient(160deg, var(--photo-light) 0%, var(--photo-mid) 100%);
  }
</style>
</head>
<body>
  <main class="ad">
    <div class="gender-tag">(M/W/D)</div>
    <h1 class="job-title">Physio-<br>therapeut</h1>
    <div class="work-model">Vollzeit / Hannover</div>
    <p class="subtitle">Werde Teil eines<br>wachsenden Teams!</p>

    <div class="brand">
      <span class="brand-name">velmo</span>
      <span class="brand-mark"></span>
    </div>

    <div class="berry-panel"></div>

    <ul class="highlights">
      <li><svg viewBox="0 0 24 24"><path d="M3 12.5l6 6L21 6" fill="none" stroke="#ffffff" stroke-width="3" stroke-linecap="round" stroke-linejoin="round"/></svg>Betriebliche KV</li>
      <li><svg viewBox="0 0 24 24"><path d="M3 12.5l6 6L21 6" fill="none" stroke="#ffffff" stroke-width="3" stroke-linecap="round" stroke-linejoin="round"/></svg>Pedalo</li>
      <li><svg viewBox="0 0 24 24"><path d="M3 12.5l6 6L21 6" fill="none" stroke="#ffffff" stroke-width="3" stroke-linecap="round" stroke-linejoin="round"/></svg>Gehalt bis 4.500 €</li>
    </ul>

    <svg class="dot-grid" width="40" height="120" viewBox="0 0 40 120" aria-hidden="true">
      <g fill="#111111">
        <circle cx="6" cy="6" r="5.5"/><circle cx="30" cy="6" r="5.5"/>
        <circle cx="6" cy="42" r="5.5"/><circle cx="30" cy="42" r="5.5"/>
        <circle cx="6" cy="78" r="5.5"/><circle cx="30" cy="78" r="5.5"/>
        <circle cx="6" cy="114" r="5.5"/><circle cx="30" cy="114" r="5.5"/>
      </g>
    </svg>

    <div class="photo" role="img" aria-label="Foto: Physiotherapeutin behandelt das angewinkelte Bein eines liegenden Patienten in einem hellen Praxisraum"></div>
  </main>
</body>
</html>
```